I need this design by August 8th or 9th!
Looking for a classy, but FUn door hangers for a community outreach "Harvest Fun Jamboree." While we are a faith-based organization, we do NOT want this to look religious. I put the LP square blue so you would have a color reference. With grey and orange as an accent color.
Event: Harvest Fun Jamboree!
Location: Calloway Meadow Estates neighborhood pavilion by the red silo.
Date: Friday, August 17th
Time: 5:30 p.m. to 8:30 p.m.
Free food, while supplies last!
Yummy desserts,
Bounce house,
Raffle,
Games and activities.

Target Market(s)

Families in the neighborhood

Colors
acd136
959595
fbee3d

Requirements
Must have
• Door hanger,

```html
<!DOCTYPE html>
<html lang="en">
<head>
<meta charset="UTF-8">
<title>Harvest Fun Jamboree – Door Hanger</title>
<link href="https://fonts.googleapis.com/css2?family=Oswald:wght@500;700&family=Roboto:wght@400;700&family=Montserrat:wght@400&family=Mr+Dafoe&display=swap" rel="stylesheet">
<style>
  :root{
    --page:#ebe8e4;
    --ink:#140d06;
    --orange:#f0911a;
    --sky-top:#f9ab3a;
    --sky-low:#e8860f;
    --grey:#d4d4d4;
    --white:#ffffff;
    --blue:#4d80a6;
  }
  *{margin:0;padding:0;box-sizing:border-box}
  html,body{width:1200px;height:1200px;overflow:hidden;background:var(--page)}
  .hanger{position:absolute;left:360px;top:30px;width:480px;height:1141px}
  .hanger-shape{position:absolute;inset:0}
  .content{position:absolute;inset:0;color:var(--white);font-family:"Roboto",Arial,sans-serif}
  .title{position:absolute;top:535px;width:100%;text-align:center;font-family:"Oswald",Impact,sans-serif;font-weight:700;font-size:48px;line-height:58px;letter-spacing:0.5px;text-transform:uppercase}
  .title .accent{color:var(--orange);display:block}
  .title .main{color:var(--grey);display:block}
  .details{position:absolute;top:683px;width:100%;text-align:center;font-size:24px}
  .details .label{color:var(--orange)}
  .date{font-weight:700}
  .time{margin-top:16px}
  .location{position:absolute;top:776px;left:62px;font-size:22px;line-height:27px}
  .location .label{color:var(--orange);font-weight:700}
  .location .addr{display:block;padding-left:128px;margin-top:-27px}
  .location .addr span{display:block}
  .offer{position:absolute;top:872px;left:62px;font-family:"Oswald",Impact,sans-serif;font-weight:700;font-size:60px;line-height:58px;text-transform:uppercase}
  .offer .free{color:var(--orange);display:block}
  .offer .food{color:var(--blue);display:block}
  .offer .note{display:block;font-weight:500;font-size:17px;line-height:22px;text-transform:none;color:var(--white);margin-top:4px;letter-spacing:-0.3px}
  .perks{position:absolute;top:892px;left:216px;list-style:none;font-family:"Montserrat",Arial,sans-serif;font-size:21px;letter-spacing:0.5px}
  .perks li{display:flex;align-items:center;height:33px}
  .perks svg{width:14px;height:14px;margin-right:10px;flex:none}
  .hashtag{position:absolute;top:1040px;width:100%;text-align:center;font-family:"Mr Dafoe",cursive;font-size:50px;color:var(--white)}
</style>
</head>
<body>
<div class="hanger">
  <svg class="hanger-shape" viewBox="0 0 480 1141" width="480" height="1141">
    <defs>
      <linearGradient id="sky" x1="0" y1="0" x2="0" y2="1">
        <stop offset="0" stop-color="var(--sky-top)"/>
        <stop offset="0.6" stop-color="#f7a233"/>
        <stop offset="1" stop-color="var(--sky-low)"/>
      </linearGradient>
    </defs>
    <rect class="photo-area" x="0" y="0" width="480" height="545" fill="url(#sky)" role="img" aria-label="Photo: silhouettes of a group of friends holding hands raised against an orange sunset sky"/>
    <path class="dark-panel" d="M0 532 Q240 498 480 532 L480 1141 L0 1141 Z" fill="var(--ink)"/>
    <path class="slit" d="M114 0 L155 0 L232 96 L196 120 Z" fill="var(--page)"/>
    <circle class="hole" cx="240" cy="179" r="99" fill="var(--page)"/>
  </svg>

  <div class="content">
    <h1 class="title"><span class="accent">Harvest Fun</span><span class="main">Jamboree</span></h1>

    <div class="details">
      <p class="date"><span class="label">DATE:</span> Friday, August 17th</p>
      <p class="time"><span class="label">Time:</span> 5:30 p.m. to 8:30 p.m.</p>
    </div>

    <p class="location"><span class="label">LOCATION:</span>
      <span class="addr"><span>Calloway Meadow Estates</span><span>&nbsp;&nbsp;neighborhood pavilion</span><span>&nbsp;&nbsp;&nbsp;&nbsp;by the red silo.</span></span>
    </p>

    <p class="offer"><span class="free">Free</span><span class="food">Food</span><span class="note">while supplies last!</span></p>

    <ul class="perks">
      <li><svg viewBox="0 0 14 14"><circle cx="7" cy="7" r="7" fill="var(--orange)"/><path d="M3.8 7.2 L6.1 9.4 L10.3 4.8" stroke="var(--ink)" stroke-width="1.8" fill="none"/></svg>Yummy desserts</li>
      <li><svg viewBox="0 0 14 14"><circle cx="7" cy="7" r="7" fill="var(--orange)"/><path d="M3.8 7.2 L6.1 9.4 L10.3 4.8" stroke="var(--ink)" stroke-width="1.8" fill="none"/></svg>Bouncy house</li>
      <li><svg viewBox="0 0 14 14"><circle cx="7" cy="7" r="7" fill="var(--orange)"/><path d="M3.8 7.2 L6.1 9.4 L10.3 4.8" stroke="var(--ink)" stroke-width="1.8" fill="none"/></svg>Raffle</li>
      <li><svg viewBox="0 0 14 14"><circle cx="7" cy="7" r="7" fill="var(--orange)"/><path d="M3.8 7.2 L6.1 9.4 L10.3 4.8" stroke="var(--ink)" stroke-width="1.8" fill="none"/></svg>Games &amp; activities</li>
    </ul>

    <p class="hashtag">#ForBrookhaven</p>
  </div>
</div>
</body>
</html>
```